Pelwick Orchards Business Cards

design business cards for our new business should match my Corvane Appraisals business cards

Contact Information for Business Card

2817 N 61st W Pl
Tulsa, OK 74389

Requirements
Must have
• should match logo colors

```html
<!DOCTYPE html>
<html lang="en">
<head>
<meta charset="UTF-8">
<title>Pelwick Orchards Business Card</title>
<link rel="stylesheet" href="https://fonts.googleapis.com/css2?family=Lato:wght@400;700;900&display=swap">
<style>
  :root {
    --bg: #2b2b2d;
    --card-white: #ffffff;
    --card-dark: #0b2a33;
    --green: #76c043;
    --teal: #1fb3ae;
    --navy: #2b2f6a;
    --rule: #cfe6c4;
    --pattern-a: #10333c;
    --pattern-b: #0d2e37;
  }
  * { margin: 0; padding: 0; box-sizing: border-box; }
  html, body { width: 1200px; height: 1108px; overflow: hidden; }
  body {
    background: var(--bg);
    font-family: "Lato", sans-serif;
    display: flex;
    align-items: center;
    justify-content: center;
    gap: 80px;
  }
  .card {
    width: 440px;
    height: 770px;
    border-radius: 30px;
    position: relative;
    overflow: hidden;
  }
  .card-front {
    background: var(--card-white);
    display: flex;
    flex-direction: column;
    align-items: center;
    text-align: center;
    color: var(--navy);
  }
  .brand {
    margin-top: 150px;
    display: flex;
    align-items: center;
    gap: 14px;
    font-weight: 900;
    font-size: 38px;
    color: var(--green);
    letter-spacing: 0.5px;
  }
  .brand-dot {
    width: 22px; height: 22px; border-radius: 50%;
    background: var(--teal);
    flex-shrink: 0;
  }
  .person-name {
    margin-top: 170px;
    font-weight: 900;
    font-size: 38px;
    color: var(--green);
    letter-spacing: 0.5px;
  }
  .person-role { font-size: 24px; margin-top: 2px; }
  .contact-divider {
    position: relative;
    width: 300px;
    margin-top: 14px;
    display: flex;
    justify-content: center;
    gap: 6px;
  }
  .contact-divider::before {
    content: ""; position: absolute; left: 0; right: 0; top: 50%;
    border-top: 1px solid var(--rule);
  }
  .icon {
    position: relative;
    width: 30px; height: 30px; border-radius: 50%;
    background: linear-gradient(135deg, var(--green), var(--teal));
    display: flex; align-items: center; justify-content: center;
    box-shadow: 0 0 0 4px var(--card-white);
  }
  .contact-list { margin-top: 14px; font-size: 24px; line-height: 34px; }
  .rule { width: 300px; border-top: 1px solid var(--rule); margin: 20px 0 16px; }
  .address { font-size: 24px; line-height: 32px; }
  .card-back { background: var(--card-dark); }
  .back-pattern {
    position: absolute; inset: 0;
    background: linear-gradient(160deg, var(--pattern-a) 0%, var(--pattern-b) 60%, var(--card-dark) 100%);
  }
  .back-brand {
    position: absolute; left: 0; right: 0; bottom: 120px;
    display: flex; justify-content: center; align-items: center; gap: 14px;
    font-weight: 900; font-size: 38px; color: var(--card-white);
    letter-spacing: 0.5px;
  }
</style>
</head>
<body>
  <section class="card card-front">
    <div class="brand"><span class="brand-dot"></span>Pelwick Orchards</div>
    <h1 class="person-name">JOHN SMITH</h1>
    <p class="person-role">Founder | CEO</p>
    <div class="contact-divider">
      <span class="icon">
        <svg width="16" height="16" viewBox="0 0 24 24"><path fill="#fff" d="M6.6 10.8a15 15 0 0 0 6.6 6.6l2.2-2.2a1 1 0 0 1 1-.25 11.4 11.4 0 0 0 3.6.57 1 1 0 0 1 1 1V20a1 1 0 0 1-1 1A17 17 0 0 1 3 4a1 1 0 0 1 1-1h3.5a1 1 0 0 1 1 1c0 1.25.2 2.45.57 3.57a1 1 0 0 1-.25 1z"/></svg>
      </span>
      <span class="icon">
        <svg width="16" height="16" viewBox="0 0 24 24"><rect x="3" y="6" width="18" height="12" rx="1" fill="none" stroke="#fff" stroke-width="2"/><path d="M3 7l9 6 9-6" fill="none" stroke="#fff" stroke-width="2"/></svg>
      </span>
      <span class="icon">
        <svg width="16" height="16" viewBox="0 0 24 24"><circle cx="12" cy="12" r="9" fill="none" stroke="#fff" stroke-width="2"/><path d="M3 12h18M12 3c3 3 3 15 0 18M12 3c-3 3-3 15 0 18" fill="none" stroke="#fff" stroke-width="1.6"/></svg>
      </span>
    </div>
    <div class="contact-list">
      <p>1234567890</p>
      <p>info@yourmail.com</p>
      <p>www.yourwebsite.com</p>
    </div>
    <div class="rule"></div>
    <div class="address">
      <p>1234 First Line Address</p>
      <p>5678 Second Line Address</p>
    </div>
  </section>

  <section class="card card-back">
    <div class="back-pattern" role="img" aria-label="Faint repeating brand pattern across the card back"></div>
    <div class="back-brand"><span class="brand-dot"></span>Pelwick Orchards</div>
  </section>
</body>
</html>
```